construction company offering modern and striking homes and apartments

I need a card design for my new construction company called Talmont Constructions (vic) Pty Ltd.
We build everything from multi home development sites to modern and edgy apartment complexes.
I am open to any colors used as long as it stands out and doesn't look cheap. I want the final design to show my prospective clients I am a professional construction company

Industry/Entity Type

Construction

```html
<!DOCTYPE html>
<html lang="en">
<head>
<meta charset="utf-8">
<title>Talmont Constructions – Business Cards</title>
<link href="https://fonts.googleapis.com/css2?family=Lato:wght@300;400;700&display=swap" rel="stylesheet">
<style>
  :root {
    --stage: #1f1f1f;
    --card-light: #f7f7f7;
    --card-dark: #2b2829;
    --ink: #3b3b3b;
    --ink-soft: #777777;
    --rule: #6a6a6a;
    --mark-dark: #2f2b2c;
    --mark-light: #e9e9e9;
    --mark-faint: #363233;
    --text-on-dark: #bdbdbd;
    --badge-green: #1f8a4c;
    --badge-navy: #1f2f6b;
    --badge-cream: #f1e7b8;
  }
  * { box-sizing: border-box; margin: 0; padding: 0; }
  html, body {
    width: 1200px; height: 997px; overflow: hidden;
    background: var(--stage);
    font-family: "Lato", sans-serif;
  }
  .stage { position: relative; width: 1200px; height: 997px; }

  .card {
    position: absolute;
    width: 560px; height: 320px;
    border-radius: 16px;
    overflow: hidden;
  }

  /* Front */
  .card--front { left: 70px; top: 130px; background: var(--card-light); color: var(--ink); }
  .front__mark {
    position: absolute; left: 44px; top: 52px;
    width: 120px; height: 120px; border-radius: 50%;
    background: var(--mark-dark);
  }
  .front__name {
    position: absolute; left: 188px; top: 66px;
    font-weight: 300; font-size: 28px; line-height: 1.05;
    letter-spacing: 2px; text-transform: uppercase; color: #555;
  }
  .front__rule {
    position: absolute; left: 188px; top: 150px;
    width: 330px; height: 2px; background: var(--rule);
  }
  .front__badges {
    position: absolute; right: 42px; top: 170px;
    display: flex; gap: 14px; align-items: center;
  }
  .badge--green { width: 46px; height: 56px; border-radius: 6px; background: var(--badge-green); }
  .badge--navy {
    width: 100px; height: 44px; background: var(--badge-navy);
    border-left: 36px solid var(--badge-cream);
  }
  .contact { position: absolute; left: 44px; top: 196px; }
  .contact__name { font-weight: 700; font-size: 19px; color: var(--ink); }
  .contact__role {
    font-size: 11px; letter-spacing: 1.5px; color: var(--ink-soft);
    text-transform: uppercase; margin-bottom: 8px;
  }
  .contact__line {
    display: flex; align-items: center; gap: 10px;
    font-size: 12.5px; color: #555; line-height: 20px;
  }
  .contact__line svg { width: 14px; height: 14px; fill: var(--ink); flex: none; }

  /* Back */
  .card--back { left: 570px; top: 500px; background: var(--card-dark); }
  .back__halo {
    position: absolute; right: -40px; top: -90px;
    width: 290px; height: 290px; border-radius: 50%;
    background: var(--mark-faint);
  }
  .back__mark {
    position: absolute; left: 44px; top: 110px;
    width: 100px; height: 100px; border-radius: 50%;
    background: var(--mark-light);
  }
  .back__name {
    position: absolute; left: 44px; top: 218px;
    font-weight: 400; font-size: 26px; line-height: 1.05;
    letter-spacing: 2px; text-transform: uppercase; color: var(--text-on-dark);
  }
  .back__web {
    position: absolute; left: 44px; top: 278px;
    font-weight: 700; font-size: 13px; letter-spacing: 1.5px; color: var(--text-on-dark);
  }
</style>
</head>
<body>
<main class="stage">

  <section class="card card--front" aria-label="Business card front">
    <div class="front__mark"></div>
    <div class="front__name">Talmont<br>Constructions</div>
    <div class="front__rule"></div>
    <div class="front__badges">
      <div class="badge--green" role="img" aria-label="Industry association badge"></div>
      <div class="badge--navy" role="img" aria-label="Builders association badge"></div>
    </div>
    <div class="contact">
      <div class="contact__name">Dana Merrow</div>
      <div class="contact__role">Owner / Founder</div>
      <div class="contact__line">
        <svg viewBox="0 0 24 24"><path d="M6.6 10.8a15 15 0 0 0 6.6 6.6l2.2-2.2a1 1 0 0 1 1-.25 11.4 11.4 0 0 0 3.6.6 1 1 0 0 1 1 1V20a1 1 0 0 1-1 1A17 17 0 0 1 3 4a1 1 0 0 1 1-1h3.5a1 1 0 0 1 1 1c0 1.25.2 2.45.6 3.6a1 1 0 0 1-.25 1z"/></svg>
        <span>03 9410 2287</span>
      </div>
      <div class="contact__line">
        <svg viewBox="0 0 24 24"><path d="M2 5h20v14H2zm2 2v.5l8 5 8-5V7l-8 5z"/></svg>
        <span>dana@talmontconstructions.com</span>
      </div>
      <div class="contact__line">
        <svg viewBox="0 0 24 24"><path d="M12 3 2 12h3v8h5v-5h4v5h5v-8h3z"/></svg>
        <span>27 Ridge Lane Westbrook vic 3041</span>
      </div>
    </div>
  </section>

  <section class="card card--back" aria-label="Business card back">
    <div class="back__halo"></div>
    <div class="back__mark"></div>
    <div class="back__name">Talmont<br>Constructions</div>
    <div class="back__web">www.talmontconstructions.com</div>
  </section>

</main>
</body>
</html>
```